Letterhead design for Sleep Consulting Business

I'm looking for a new letterhead (heading/footer) design for my Sleep Consulting Business, I work with families to help their children improve their sleep.

The heading/footer will used in Microsoft Word Only-to be used for all of my documents such as writing Sleep Plans. I need to utilize as much working space in the document as possible. This will NOT be printed out on paper- it will only be used for heading/footer on microsoft word, then emailed to clients, who may print it at home.

My brand colors:
Dark Blue Hex: 1F2A42
Lighter Blueish Hex: 90BEC9
You're welcome to check out my website for inspiration- it is freshly created with other colors as well, and I love the outcome. www.hollowpinerest.com

Target Market(s)

Tired parents

Font styles to use
Script
Other font styles liked:
• Great Vibe, Lato or Just Another Hand are all used currently for my brand. Open to other options.

Requirements
Must have
• The letterhead (heading/footer) MUST be kept narrow (height-wise), so I have plenty of space on my document, while including important information.

It should look professional on screen, and when printed.

Must include my business name OR logo (Hollow Pine Sleep Consulting), and my email address. Mara@hollowpinerest.com

Website is optional, not required, just if you need to fill in a spot: www.hollowpinerest.com

```html
<!DOCTYPE html>
<html lang="en">
<head>
<meta charset="utf-8">
<title>Hollow Pine Sleep Consulting – Letterhead</title>
<link href="https://fonts.googleapis.com/css2?family=Lato:wght@400;700&family=Open+Sans:wght@400;600&display=swap" rel="stylesheet">
<style>
  :root {
    --navy: #1F2A42;
    --sky: #90BEC9;
    --ink: #3a3a3a;
    --paper: #ffffff;
    --backdrop: #e6e7e9;
    --sign-tone: #e4e7ec;
  }
  html, body {
    margin: 0;
    width: 1040px;
    height: 1200px;
    overflow: hidden;
    background: var(--backdrop);
  }
  .letter {
    position: absolute;
    left: 69px;
    top: 20px;
    width: 798px;
    height: 1027px;
    background: var(--paper);
    transform: scale(1.13);
    transform-origin: 0 0;
    overflow: hidden;
    font-family: "Open Sans", Arial, sans-serif;
    color: var(--ink);
    font-size: 12.5px;
    box-shadow: 0 2px 10px rgba(0,0,0,0.15);
  }
  .brand {
    position: absolute;
    left: 78px;
    top: 28px;
    display: flex;
    align-items: center;
    gap: 14px;
  }
  .brand-dot {
    width: 58px;
    height: 58px;
    border-radius: 50%;
    background: var(--navy);
  }
  .brand-name {
    font-family: "Lato", Arial, sans-serif;
    font-weight: 700;
    font-size: 19px;
    color: var(--navy);
    line-height: 1.2;
    width: 190px;
  }
  .header-email {
    position: absolute;
    right: 67px;
    top: 50px;
    font-family: "Lato", Arial, sans-serif;
    font-weight: 700;
    font-size: 15px;
    color: #111;
  }
  .body {
    position: absolute;
    left: 75px;
    top: 200px;
    width: 645px;
  }
  .body p { margin: 0; }
  .issue-date { margin-bottom: 14px !important; }
  .recipient { margin-bottom: 44px !important; line-height: 15.5px; }
  .salutation { margin-bottom: 22px !important; }
  .body p.para {
    margin-bottom: 23px;
    line-height: 23px;
    text-align: justify;
    hyphens: auto;
    -webkit-hyphens: auto;
  }
  .closing { margin: 42px 0 8px !important; }
  .signature {
    width: 185px;
    height: 24px;
    background: var(--sign-tone);
    border-radius: 3px;
  }
  .signer-name {
    margin: 8px 0 4px !important;
    font-size: 15.5px;
    color: #222;
  }
  .footer {
    position: absolute;
    left: 0;
    top: 887px;
    width: 798px;
    height: 140px;
  }
  .footer-stripe {
    position: absolute;
    left: 0;
    top: 26px;
    width: 100%;
    height: 8px;
    background: var(--sky);
  }
  .footer-band {
    position: absolute;
    left: 0;
    top: 40px;
    width: 100%;
    height: 100px;
    background: var(--navy);
  }
  .footer-web {
    position: absolute;
    right: 66px;
    top: 88px;
    font-family: "Lato", Arial, sans-serif;
    font-size: 15px;
    color: #fff;
  }
</style>
</head>
<body>
  <main class="letter">
    <header>
      <div class="brand">
        <span class="brand-dot"></span>
        <span class="brand-name">Hollow Pine Sleep Consulting</span>
      </div>
      <div class="header-email">Mara@hollowpinerest.com</div>
    </header>

    <section class="body">
      <p class="issue-date">Issuing Date: May 5, 2018</p>
      <p class="recipient">Name Of Employee Mr. XYZABC<br>Address of Employee<br>Address Line 2 etc..</p>
      <p class="salutation">Dear Mr.XYZABC</p>
      <p class="para">Lorem Ipsum has been the industry's standard dummy text ever since the 1500s, when an unknown printer took a galley of type and scrambled it to make a type specimen book. It has survived not only five centuries, but also the leap into electronic typesetting, remaining essentially unchanged. It was popularised in the 1960s with the release of Linotrace sheets containing Lorem Ipsum passages, and more recently with desktop publishing software like Folio PageSetter including versions of Lorem Ipsum.</p>
      <p class="para">Lorem Ipsum is simply dummy text of the printing and typesetting industry. Lorem Ipsum has been the industry's standard dummy text ever since the 1500s, when an unknown printer took a galley of type and scrambled it to make a type specimen book.</p>
      <p class="para">It has survived not only five centuries, but also the leap into electronic typesetting, remaining essentially unchanged. It was popularised in the 1960s with the release of Linotrace sheets containing Lorem IpsumIpsum passages.</p>
      <p class="closing">Yours Sincerely</p>
      <div class="signature" role="img" aria-label="Handwritten signature of Daniel Carter"></div>
      <p class="signer-name">Daniel Carter</p>
      <p class="signer-role">Managing Director</p>
    </section>

    <footer class="footer">
      <div class="footer-stripe"></div>
      <div class="footer-band"></div>
      <div class="footer-web">www.hollowpinerest.com</div>
    </footer>
  </main>
</body>
</html>
```